Township of Harlowden E-Alert Signup

Need to create print media that is designed for a Town in New Jersey that is starting a marketing campaign to get townspeople to sign up for the E-Alert system.Need print media that is 1. interchangeable in size (regular letter-size, as well as a poster size) 2. Branded with their colors, logo, etc. (green and white displayed in logo)3. Displays the incentives to sign up. Incentives:- Community Services/Announcements- Gov’t/Non-profit Resources- Tax Information- Employment opportunities- Municipal Services/Public Works/Recreation Divisions- Health Updates
Target Market(s)
Townspeople of Maplewood NJ
Industry/Entity Type
Government
Colors
Designer to choose colors to be used in the design.
Requirements
Must have
- 1. interchangeable in size (regular letter-size, as well as a poster size)
- 2. Branded with their colors, logo, etc. (green and white displayed in logo)
- 3. Displays the incentives to sign up.
- Incentives:
- - Community Services/Announcements
- - Gov’t/Non-profit Resources
- - Tax Information
- - Employment opportunities
- - Municipal Services/Public Works/Recreation Divisions
- - Health Updates

```html
<!DOCTYPE html>
<html lang="en">
<head>
<meta charset="utf-8">
<title>Township of Harlowden E-alert Signup</title>
<link href="https://fonts.googleapis.com/css2?family=Barlow:ital,wght@0,700;1,700&family=Lato:wght@400;700&display=swap" rel="stylesheet">
<style>
  :root {
    --green-dark: #0a6630;
    --green-mid: #2f8a3a;
    --green-light: #6aa84a;
    --gold: #f2c417;
    --gold-deep: #c9961e;
    --white: #ffffff;
    --stage: #eeeeea;
    --photo-sky: #5d6fb0;
    --photo-stone: #8a8077;
    --photo-road: #6e6e70;
  }
  html, body {
    margin: 0;
    width: 946px;
    height: 1200px;
    overflow: hidden;
    background: var(--stage);
  }
  .poster {
    position: absolute;
    left: 55px;
    top: 10px;
    width: 836px;
    height: 1180px;
    overflow: hidden;
    background: radial-gradient(ellipse at 45% 55%, var(--green-light) 0%, var(--green-mid) 45%, var(--green-dark) 100%);
  }
  .poster-art {
    position: absolute;
    inset: 0;
  }
  .headline {
    position: absolute;
    left: 62px;
    top: 40px;
    margin: 0;
    color: var(--white);
    font-family: "Barlow", sans-serif;
    font-weight: 700;
    line-height: 1;
  }
  .headline-kicker {
    display: block;
    font-style: italic;
    font-size: 40px;
    letter-spacing: -0.5px;
  }
  .headline-main {
    display: block;
    font-size: 54px;
    margin-top: 10px;
    letter-spacing: -0.5px;
  }
  .seal {
    position: absolute;
    left: 48px;
    top: 530px;
    width: 270px;
    height: 270px;
    border-radius: 50%;
    background: var(--white);
    display: flex;
    align-items: center;
    justify-content: center;
    text-align: center;
  }
  .seal-name {
    font-family: "Lato", sans-serif;
    font-weight: 700;
    font-size: 27px;
    line-height: 1.2;
    color: var(--green-dark);
  }
  .incentives {
    position: absolute;
    left: 49px;
    top: 855px;
    color: var(--white);
    font-family: "Lato", sans-serif;
  }
  .incentives-title {
    margin: 0 0 18px;
    font-size: 35px;
    font-weight: 700;
  }
  .incentives-list {
    list-style: none;
    margin: 0;
    padding: 0;
    font-size: 25px;
    line-height: 33.5px;
  }
  .incentives-list li::before {
    content: "\2022";
    margin-right: 9px;
  }
</style>
</head>
<body>
  <main class="poster">
    <svg class="poster-art" viewBox="0 0 836 1180" width="836" height="1180" aria-hidden="false">
      <defs>
        <linearGradient id="street-photo" x1="0" y1="0" x2="0" y2="1">
          <stop offset="0" stop-color="var(--photo-sky)"/>
          <stop offset="0.45" stop-color="var(--photo-stone)"/>
          <stop offset="1" stop-color="#4a4744"/>
        </linearGradient>
        <radialGradient id="crosswalk-photo" cx="0.5" cy="0.5" r="0.6">
          <stop offset="0" stop-color="var(--photo-road)"/>
          <stop offset="1" stop-color="#7f8a6e"/>
        </radialGradient>
        <linearGradient id="gold-band" x1="0" y1="0" x2="1" y2="0">
          <stop offset="0" stop-color="var(--gold-deep)"/>
          <stop offset="0.5" stop-color="var(--gold)"/>
          <stop offset="1" stop-color="var(--gold-deep)"/>
        </linearGradient>
      </defs>

      <!-- upper gold wave -->
      <path class="wave-gold-top" d="M0,262 C200,300 420,236 560,166 C680,108 780,98 836,104 L836,118 C780,112 680,124 560,186 C420,258 200,318 0,296 Z" fill="url(#gold-band)"/>

      <!-- downtown street photo -->
      <path class="photo-street" role="img" aria-label="Photo of downtown street with brick storefront buildings"
            d="M0,300 C200,320 420,262 560,192 C680,130 780,120 836,122 L836,538 C700,530 520,590 330,628 C180,656 70,650 0,640 Z"
            fill="url(#street-photo)"/>

      <!-- lower gold line under photo -->
      <path class="wave-gold-mid" d="M0,640 C70,650 180,656 330,628 C520,590 700,530 836,536 L836,552 C700,548 520,608 330,646 C180,674 70,668 0,660 Z" fill="url(#gold-band)"/>

      <!-- white swoosh -->
      <path class="wave-white" d="M300,700 C420,680 540,690 640,700 L836,760 L836,840 C700,800 560,760 470,745 C400,733 350,720 300,700 Z" fill="var(--white)"/>
      <path class="wave-gold-swoosh" d="M300,700 C380,730 450,745 520,780 C560,800 600,830 630,860 C580,820 520,790 460,770 C400,750 350,730 300,700 Z" fill="var(--gold-deep)"/>

      <!-- lower right gold band -->
      <path class="wave-gold-bottom" d="M520,905 C640,960 760,1010 836,1062 L836,1040 C760,990 640,945 520,905 Z" fill="url(#gold-band)"/>
      <path class="wave-white-bottom" d="M600,900 C700,930 780,960 836,990 L836,1040 C760,990 680,950 600,900 Z" fill="var(--white)"/>

      <!-- crosswalk photo circle -->
      <circle class="photo-ring" cx="668" cy="752" r="184" fill="var(--white)"/>
      <circle class="photo-crosswalk" role="img" aria-label="Aerial photo of a rainbow-painted crosswalk intersection"
              cx="668" cy="752" r="176" fill="url(#crosswalk-photo)"/>
    </svg>

    <h1 class="headline">
      <span class="headline-kicker">SIGN UP FOR THE</span>
      <span class="headline-main">E-alert System</span>
    </h1>

    <div class="seal">
      <span class="seal-name">Township of<br>Harlowden</span>
    </div>

    <section class="incentives">
      <h2 class="incentives-title">Incentives To Sign Up</h2>
      <ul class="incentives-list">
        <li>Community Services/Announcements</li>
        <li>Gov’t/Non-profit Resources</li>
        <li>Tax Information</li>
        <li>Employment opportunities</li>
        <li>Municipal Services/Public Works/Recreation Divisions</li>
        <li>Health Updates</li>
      </ul>
    </section>
  </main>
</body>
</html>
```